Full Stationary
Business Cards & Stationery for Limo Service - Transportation
Business Cards & Stationery for Limo Service
Professional
Glen Harbury / Dale Pronto
President / General Manager
1187 Fenwick Blvd, Suite 300 Des Moines, IA 50317
844.RQT.CARZ
info@vantregocars.example
www.vantregocars.example
I don't want this card to be too cluttered but I want it to look super sharp and modern. I like modern font however I want it to remain similar to the logo and professional as we are handing these cards to operators throughout the United States.
Be creative. I am unsure of the future demand for QR codes. I have attached 3, one for the website, Facebook, and Twitter. Feel free to use them if you wish, however, if there is something new I am unaware of please feel free to use this new technology. As stated earlier, I am unsure how well these work in todays world versus a few years ago. I have used them previously on the backs of business cards and think it looks cool, however if I am mistaken of something different please let me know.

```html
<!DOCTYPE html>
<html lang="en">
<head>
<meta charset="utf-8">
<title>Vantrego Cars – Business Card</title>
<link href="https://fonts.googleapis.com/css2?family=Montserrat:wght@400;500;600&display=swap" rel="stylesheet">
<style>
  :root {
    --page: #eceef0;
    --card: #ffffff;
    --ink: #3a3c40;
    --ink-soft: #6b6e73;
    --silver-dark: #5c5f64;
    --silver: #a9acb1;
    --silver-light: #d9dbde;
    --accent: #3d4f8f;
    --shadow: rgba(0,0,0,0.14);
  }
  * { box-sizing: border-box; margin: 0; padding: 0; }
  html, body {
    width: 1200px; height: 939px; overflow: hidden;
    background: var(--page);
    font-family: "Montserrat", sans-serif;
    color: var(--ink);
  }
  .sheet {
    position: relative; width: 1200px; height: 939px;
    display: flex; align-items: center; justify-content: center; gap: 60px;
  }
  .card {
    position: relative; width: 520px; height: 297px;
    background: var(--card);
    box-shadow: 0 10px 28px var(--shadow);
    overflow: hidden;
  }
  .wordmark {
    display: flex; align-items: center; gap: 12px;
  }
  .wordmark__square {
    width: 34px; height: 34px; background: var(--silver-dark);
  }
  .wordmark__name {
    font-weight: 500; font-size: 24px; letter-spacing: 0.22em;
    color: var(--silver-dark); text-transform: uppercase;
  }
  /* front */
  .card--front { display: flex; align-items: center; justify-content: center; }
  /* back */
  .card--back .wordmark { position: absolute; left: 30px; top: 32px; }
  .card--back .wordmark__square { width: 30px; height: 30px; }
  .card--back .wordmark__name { font-size: 20px; }
  .address {
    position: absolute; left: 30px; top: 86px;
    font-size: 9.5px; line-height: 1.5; color: var(--ink-soft);
  }
  .person {
    position: absolute; right: 30px; top: 96px; text-align: right;
  }
  .person__name { font-weight: 600; font-size: 15px; color: var(--ink); }
  .person__role { font-size: 12px; color: var(--ink-soft); margin-top: 2px; }
  .contacts {
    position: absolute; right: 30px; top: 150px;
    list-style: none; font-size: 10px; line-height: 1.75; color: var(--ink-soft); text-align: right;
  }
  .contacts li { display: flex; align-items: center; justify-content: flex-end; gap: 6px; }
  .contacts svg { width: 9px; height: 9px; fill: var(--ink); }
  .swoosh { position: absolute; left: 0; bottom: 0; width: 520px; height: 150px; }
  .website {
    position: absolute; right: 32px; bottom: 14px;
    font-size: 9.5px; letter-spacing: 0.04em; color: #f2f3f5;
  }
</style>
</head>
<body>
<main class="sheet">
  <section class="card card--front" aria-label="Card front">
    <div class="wordmark">
      <span class="wordmark__square"></span>
      <span class="wordmark__name">Vantrego Cars</span>
    </div>
  </section>

  <section class="card card--back" aria-label="Card back">
    <svg class="swoosh" viewBox="0 0 520 150" preserveAspectRatio="none" aria-hidden="true">
      <defs>
        <linearGradient id="silverBand" x1="0" y1="0" x2="1" y2="0">
          <stop offset="0" stop-color="#4e5156"/>
          <stop offset="0.45" stop-color="#9a9da2"/>
          <stop offset="0.75" stop-color="#6e7176"/>
          <stop offset="1" stop-color="#3f4246"/>
        </linearGradient>
        <linearGradient id="silverSoft" x1="0" y1="0" x2="1" y2="0">
          <stop offset="0" stop-color="#c9cbce"/>
          <stop offset="1" stop-color="#eeeff1"/>
        </linearGradient>
      </defs>
      <path d="M0 40 C140 95 330 120 520 70 L520 150 L0 150 Z" fill="url(#silverSoft)"/>
      <path d="M0 62 C150 120 340 135 520 92 L520 150 L0 150 Z" fill="url(#silverBand)"/>
      <path d="M0 34 C140 88 330 112 520 62" stroke="#2f3135" stroke-width="2" fill="none"/>
      <path d="M200 150 C330 140 440 118 520 96" stroke="var(--accent)" stroke-width="3" fill="none"/>
    </svg>

    <div class="wordmark">
      <span class="wordmark__square"></span>
      <span class="wordmark__name">Vantrego Cars</span>
    </div>

    <address class="address">
      1187 Fenwick Blvd, Suite 300<br>
      Des Moines, IA<br>
      50317 USA
    </address>

    <div class="person">
      <p class="person__name">Glen Harbury</p>
      <p class="person__role">Consultant</p>
    </div>

    <ul class="contacts">
      <li>844.RQT.CARZ
        <svg viewBox="0 0 10 10"><path d="M2 0.5 L4 2.5 L3 3.8 C3.6 5.2 4.8 6.4 6.2 7 L7.5 6 L9.5 8 L8.2 9.5 C4 9 1 6 0.5 1.8 Z"/></svg>
      </li>
      <li>515.208.4410
        <svg viewBox="0 0 10 10"><rect x="2.5" y="0.5" width="5" height="9" rx="1"/></svg>
      </li>
      <li>info@vantregocars.example
        <svg viewBox="0 0 10 10"><path d="M0.5 2 H9.5 V8 H0.5 Z M0.5 2 L5 5.5 L9.5 2" stroke="#3a3c40" stroke-width="0.8" fill="none"/></svg>
      </li>
    </ul>

    <p class="website">www.vantregocars.example</p>
  </section>
</main>
</body>
</html>
```